Store Front Signage for an Upscale Cake & Dessert Bakery

We need a design for store front windows. We are a 12 year old bakery specializing in cakes, cupcakes, cookies, pies, and other desserts. We recently moved to a high traffic location.. and we would like to boost our visual presence; we can be seen from the main road but are competing with other businesses for attention. Attached is a photo of our store front with posters but this signage will be for window film for the entire window span. (see the store front to the left of the photo to see the green and yellow as a film example)
Our logo and store sign (not like in photo, that is showing more red) are in shades of pink. The most visible part of the signage is in the upper third to upper half of the 60" panels.
The signs in the window currently say Life's Short. Eat Cake.
We now use Enjoy Life. Eat Cake.
The design should span all the windows and door -- this can be individual panels or one design that covers all panels. I have pink and greys chosen but please DO NOT let this constrain you. The inside of the bakery has grey floors and walls. white cabinetry, black granite countertops. The only thing with color is the baked goods and display cakes, pictures of cakes, the logo and menu and employee shirts.

Target Market(s)

we are located at a busy intersection --- we would like to capture the attention of people in cars as they pass by and entice them to stop in

Font styles to use
Serif
Sans Serif

Colors
d3d3d3
757575
ffffff
e24197
e667a6
eea4c8
f9d9e8

Requirements
Must have
• I would like the design to be easily discernible at the road way that is about 75 feet from store front. If you look at the photos I provide, note that the font size that is easily readable from the road are the ones in the top panes (although the shadow from the building makes them difficult to see -- the best visibility is the top 1/3 of the 60" panels.
Nice to have
• would like to have some non-photo graphics of a cake ( like a birthday cake), tiered cake, cupcakes, and cookies or pie for the panels --- but DO NOT let this constrain you. I need something to grab attention while cars are stopped at the nearby traffic light.
• If this design works well... I will be changing the panel on a seasonal basis
Should not have
• words that cannot be read from a distance.

```html
<!DOCTYPE html>
<html lang="en">
<head>
<meta charset="utf-8">
<title>Rosabelle's Bake Shoppe – Window Film</title>
<link rel="stylesheet" href="https://fonts.googleapis.com/css2?family=Noticia+Text:wght@400;700&family=Roboto+Condensed:wght@700&display=swap">
<style>
  :root {
    --page: #ececec;
    --frame: #1b1b1b;
    --film-black: #121212;
    --film-grey: #2e2e2e;
    --awning-plum: #9a2a7c;
    --awning-mauve: #c98bb6;
    --awning-light: #f3e4ee;
    --lace-plum: #a3338a;
    --lace-pink: #c76aae;
    --logo-pink: #eea4c8;
    --accent-pink: #e667a6;
    --text-white: #ffffff;
  }
  * { box-sizing: border-box; margin: 0; padding: 0; }
  html, body { width: 1200px; height: 1000px; overflow: hidden; background: var(--page); }
  body { display: flex; align-items: center; justify-content: center; }

  .window-span {
    display: grid;
    grid-template-columns: 226px 223px 157px 226px 228px;
    grid-template-rows: 138px 297px 82px;
    gap: 10px;
    padding: 8px;
    background: var(--frame);
  }

  /* Awning row: artwork area held as a soft tonal fill */
  .awning {
    background: var(--film-black);
    padding-top: 4px;
  }
  .awning-art {
    height: 92px;
    border-radius: 0 0 12px 12px;
    background: linear-gradient(180deg, var(--awning-plum) 0%, #b35d9c 45%, var(--awning-mauve) 75%, var(--awning-light) 100%);
  }

  /* Main film panel */
  .film-panel {
    position: relative;
    overflow: hidden;
  }
  .damask-field {
    position: absolute; inset: 0;
    background:
      radial-gradient(ellipse at 30% 25%, var(--film-grey) 0%, transparent 55%),
      radial-gradient(ellipse at 75% 70%, var(--film-grey) 0%, transparent 55%),
      var(--film-black);
  }
  .panel-copy {
    position: relative;
    height: 100%;
    display: flex;
    flex-direction: column;
    align-items: center;
    justify-content: center;
    text-align: center;
    color: var(--text-white);
    font-family: "Noticia Text", Georgia, serif;
  }

  .brand-mark { display: flex; align-items: center; gap: 8px; }
  .brand-dot { width: 14px; height: 14px; border-radius: 50%; background: var(--logo-pink); }
  .brand-name {
    font-weight: 700;
    color: var(--logo-pink);
    font-size: 25px;
    letter-spacing: 0.5px;
  }
  .shop-title { font-size: 35px; line-height: 36px; margin-top: 12px; }
  .title-rule { width: 68px; height: 2px; background: var(--accent-pink); margin-top: 14px; }

  .offer { font-size: 22px; line-height: 23px; }
  .offer-dot {
    width: 15px; height: 15px; border-radius: 50%;
    background: var(--logo-pink);
    margin: 12px 0;
  }
  .fine-print {
    font-family: "Roboto Condensed", Arial, sans-serif;
    font-weight: 700;
    font-size: 13.5px;
    line-height: 15px;
    margin-top: 20px;
  }

  .door .brand-name { font-size: 17px; }
  .door .brand-dot { width: 10px; height: 10px; }
  .door .shop-title { font-size: 22px; line-height: 23px; margin-top: 8px; }
  .door .title-rule { width: 44px; margin-top: 10px; }
  .door .fine-print { font-size: 10.5px; line-height: 12px; margin-top: 14px; }

  /* Lace band: ornament area held as a soft tonal fill */
  .lace-band {
    background: linear-gradient(180deg, var(--lace-pink) 0%, var(--lace-plum) 35%, #8c2673 100%);
  }
</style>
</head>
<body>
  <main class="window-span">
    <div class="awning"><div class="awning-art" role="img" aria-label="Striped plum and white shop awning"></div></div>
    <div class="awning"><div class="awning-art" role="img" aria-label="Striped plum and white shop awning"></div></div>
    <div class="awning"><div class="awning-art" role="img" aria-label="Striped plum and white shop awning"></div></div>
    <div class="awning"><div class="awning-art" role="img" aria-label="Striped plum and white shop awning"></div></div>
    <div class="awning"><div class="awning-art" role="img" aria-label="Striped plum and white shop awning"></div></div>

    <section class="film-panel">
      <div class="damask-field" role="img" aria-label="Dark grey damask scroll pattern on black"></div>
      <div class="panel-copy">
        <div class="brand-mark"><span class="brand-dot"></span><span class="brand-name">Rosabelle's</span></div>
        <p class="shop-title">bake<br>shoppe</p>
        <div class="title-rule"></div>
      </div>
    </section>

    <section class="film-panel">
      <div class="damask-field" role="img" aria-label="Dark grey damask scroll pattern on black"></div>
      <div class="panel-copy">
        <p class="offer">custom<br>cakes</p>
        <span class="offer-dot"></span>
        <p class="offer">holiday<br>desserts</p>
        <span class="offer-dot"></span>
        <p class="fine-print">ORDER ONLINE<br>ROSABELLES.COM</p>
      </div>
    </section>

    <section class="film-panel door">
      <div class="damask-field" role="img" aria-label="Dark grey damask scroll pattern on black"></div>
      <div class="panel-copy">
        <div class="brand-mark"><span class="brand-dot"></span><span class="brand-name">Rosabelle's</span></div>
        <p class="shop-title">bake<br>shoppe</p>
        <div class="title-rule"></div>
        <p class="fine-print">HOURS:<br>MONDAY-SATURDAY<br>9AM - 7PM<br>SUNDAY 11AM-5PM</p>
      </div>
    </section>

    <section class="film-panel">
      <div class="damask-field" role="img" aria-label="Dark grey damask scroll pattern on black"></div>
      <div class="panel-copy">
        <p class="offer">cupcakes<br>galore</p>
        <span class="offer-dot"></span>
        <p class="offer">sweets and<br>cookies</p>
        <span class="offer-dot"></span>
        <p class="fine-print">NEXT DAY PICK-UP<br>DELIVERY AVAILABLE</p>
      </div>
    </section>

    <section class="film-panel">
      <div class="damask-field" role="img" aria-label="Dark grey damask scroll pattern on black"></div>
      <div class="panel-copy">
        <div class="brand-mark"><span class="brand-dot"></span><span class="brand-name">Rosabelle's</span></div>
        <p class="shop-title">bake<br>shoppe</p>
        <div class="title-rule"></div>
      </div>
    </section>

    <div class="lace-band" role="img" aria-label="Plum lace border with fleur ornaments"></div>
    <div class="lace-band" role="img" aria-label="Plum lace border with fleur ornaments"></div>
    <div class="lace-band" role="img" aria-label="Plum lace border with fleur ornaments"></div>
    <div class="lace-band" role="img" aria-label="Plum lace border with fleur ornaments"></div>
    <div class="lace-band" role="img" aria-label="Plum lace border with fleur ornaments"></div>
  </main>
</body>
</html>
```